Letterhead Design Project

Standard A4 paper, center the name Brightway Wash (with the mop) same as front of business card.
47 Harbour Vale Rd Kelston 5062 ABN: 71205839416
M. 0427163958 T. 83917605 Calibri font

Industry/Entity Type

Business

```html
<!DOCTYPE html>
<html lang="en">
<head>
<meta charset="utf-8">
<title>Brightway Wash Letterhead</title>
<link rel="stylesheet" href="https://fonts.googleapis.com/css2?family=Open+Sans:wght@400;700&display=swap">
<style>
  :root {
    --canvas: #ffffff;
    --page: #ffffff;
    --page-border: #4a4a4a;
    --brand-blue: #3d3f91;
    --rule-grey: #8c8c8c;
    --body-text: #333333;
    --abn-red: #e0383e;
    --mark-tone: #9fd3d6;
  }
  * { margin: 0; padding: 0; box-sizing: border-box; }
  html, body {
    width: 1200px;
    height: 1002px;
    overflow: hidden;
    background: var(--canvas);
    font-family: "Open Sans", Arial, sans-serif;
  }
  .letterhead {
    position: absolute;
    left: 213px;
    top: 0;
    width: 775px;
    height: 1002px;
    background: var(--page);
    border: 1px solid var(--page-border);
  }
  .brand-mark {
    position: absolute;
    left: 62px;
    top: 52px;
    width: 70px;
    height: 70px;
    background: var(--mark-tone);
  }
  .brand-name {
    position: absolute;
    left: 175px;
    top: 50px;
    width: 508px;
    font-size: 55px;
    line-height: 62px;
    font-weight: 700;
    color: var(--brand-blue);
    white-space: nowrap;
    letter-spacing: 0.5px;
    text-align: center;
  }
  .header-rule {
    position: absolute;
    left: 179px;
    top: 116px;
    width: 498px;
    height: 2px;
    background: var(--rule-grey);
  }
  .contact-line {
    position: absolute;
    left: 213px;
    top: 122px;
    font-size: 13px;
    line-height: 18px;
    color: var(--body-text);
    white-space: nowrap;
  }
  .contact-line .phone { margin-left: 10px; }
  .abn {
    position: absolute;
    right: 51px;
    top: 159px;
    font-size: 13px;
    line-height: 18px;
    color: var(--abn-red);
  }
</style>
</head>
<body>
  <main class="letterhead">
    <header class="letterhead-header">
      <div class="brand-mark" role="img" aria-label="Cleaning tools illustration: mop, bucket and broom"></div>
      <h1 class="brand-name">BRIGHTWAY WASH</h1>
      <div class="header-rule"></div>
      <p class="contact-line">47, Harbour Vale Road, Kelston-5062<span class="phone">Mob. 0427163958 T. 83917605</span></p>
      <p class="abn">ABN: 71205839416</p>
    </header>
  </main>
</body>
</html>
```